Update Product Descriptions on Existing Website

We need to update product descriptions and images on three pages of our existing website. The tables are in editable HTML format. The formatting will be the exact same, just need the descriptions and images updated.

I have included the source documents below.

Coding

Coded - Design and coding required

Number of Pages Required

3 page

Colors

Designer to choose colors to be used in the design.

```html
<!DOCTYPE html>
<html lang="en">
<head>
<meta charset="utf-8">
<title>Molded Grating</title>
<link rel="stylesheet" href="https://fonts.googleapis.com/css2?family=Open+Sans:wght@400;700&display=swap">
<style>
:root{
  --ink:#222;
  --rule:#111;
  --link:#2a8be8;
  --brand:#8b1f86;
  --accent:#e0261d;
  --stripe:#f2f2f2;
  --line:#dcdcdc;
  --divider:#999;
  --mesh-a:#2f7a63;
  --mesh-b:#5fa88f;
}
*{box-sizing:border-box;margin:0;padding:0}
html,body{width:1200px;height:675px;overflow:hidden;background:#fff}
body{font-family:"Open Sans",Arial,sans-serif;color:var(--ink);position:relative}

.caption{position:absolute;left:0;width:1200px;text-align:center;font-size:13.5px;line-height:18px;white-space:nowrap}
.caption--legacy{top:1px}
.caption--modern{top:244px}

.tag{position:absolute;top:23px;left:0;width:179px;height:41px;background:var(--brand);color:#fff;font-size:21px;line-height:41px;padding-left:26px;z-index:2}

.legacy{position:absolute;top:34px;left:0;width:1199px;border-collapse:collapse;table-layout:fixed;font-size:13px}
.legacy td{border:1px solid var(--rule);padding:0 1px;height:19.2px;line-height:17px;white-space:nowrap;overflow:hidden}
.legacy .head td{height:111px;vertical-align:top;padding:0}
.legacy .label-cell{position:relative;font-size:13.5px}
.legacy .label-cell span{position:absolute;left:2px;top:49px}
.product{display:flex;height:110px}
.product a{display:block;width:110px;height:100%;border-right:1px solid var(--divider);color:var(--link);text-decoration:none;font-size:13.5px;line-height:18.5px;padding:5px 3px;white-space:normal}

.modern{position:absolute;top:277px;left:0;width:1199px;border-collapse:collapse;table-layout:fixed;font-size:13px}
.modern td{border:1px solid var(--line);padding:0 5px;height:28px;vertical-align:middle;white-space:nowrap}
.modern tr:nth-child(even) td{background:var(--stripe)}
.modern .head td{height:114px;padding:0;background:#fff}
.modern .key{font-weight:700}
.intro{position:relative;height:113px}
.intro .title{position:absolute;left:34px;top:18px;color:var(--accent);font-size:20px;line-height:24px}
.intro .hint{position:absolute;left:5px;top:91px;font-weight:700;font-size:13px;line-height:18px}
.shot{display:block;width:130px;height:86px;margin:0 auto;border-radius:6px;background:linear-gradient(135deg,var(--mesh-b),var(--mesh-a))}
</style>
</head>
<body>
<p class="caption caption--legacy">The following sizes and types of molded grating are available from KRV:</p>
<div class="tag">Your Design</div>
<table class="legacy">
  <colgroup><col style="width:306px"><col><col><col><col><col></colgroup>
  <tr class="head">
    <td class="label-cell"><span>Profile Image (click to enlarge)</span></td>
    <td><div class="product"><a href="#">Molded Grating 0.5in thick 1.5x1.5 mesh</a></div></td>
    <td><div class="product"><a href="#">Molded Grating 0.5in thick 1.5x1.5 mesh</a></div></td>
    <td><div class="product"><a href="#">Molded Grating 0.5in thick 0.75x0.75 mesh</a></div></td>
    <td><div class="product"><a href="#">Molded Grating 0.75in thick 1.5x1.5 mesh</a></div></td>
    <td><div class="product"><a href="#">Molded Grating 1in thick 1.5x1.5 mesh</a></div></td>
  </tr>
  <tr><td>Height(in.)</td><td>0.5</td><td>0.5</td><td>0.5</td><td>0.75</td><td>1</td></tr>
  <tr><td>Mesh Size (in.)</td><td>2x2</td><td>1.5x1.5</td><td>.75x.75 1.5x1.5</td><td>1.5x1.5</td><td>1.5x1.5</td></tr>
  <tr><td>Standard Panel Size(ft.)</td><td>12x4</td><td>12.4</td><td>12.5x4</td><td>12x4</td><td>10x4, 12x4</td></tr>
  <tr><td>Open Area</td><td>74%</td><td>72%</td><td>42%</td><td>69%</td><td>69%</td></tr>
  <tr><td>Weight (lbs./ft.)</td><td>1.02</td><td>1.33</td><td>2.15</td><td>1.88</td><td>2.52</td></tr>
</table>

<p class="caption caption--modern">The following sizes and types of molded grating are available from KRV:</p>
<table class="modern">
  <colgroup><col style="width:266px"><col><col><col><col><col></colgroup>
  <tr class="head">
    <td><div class="intro"><p class="title">New Design<br>with bootstrap</p><p class="hint">Profile Image (click to enlarge)</p></div></td>
    <td><span class="shot" role="img" aria-label="Molded grating panel, 2x2 mesh"></span></td>
    <td><span class="shot" role="img" aria-label="Molded grating panel, 1.5x1.5 mesh"></span></td>
    <td><span class="shot" role="img" aria-label="Molded grating panel, 0.75x0.75 mesh"></span></td>
    <td><span class="shot" role="img" aria-label="Molded grating panel, 0.75in thick"></span></td>
    <td><span class="shot" role="img" aria-label="Molded grating panel, 1in thick"></span></td>
  </tr>
  <tr><td class="key">Height (in.)</td><td>0.5</td><td>0.5</td><td>0.5</td><td>0.5</td><td>0.5</td></tr>
  <tr><td class="key">Mesh Size (in.)</td><td>2x2</td><td>1.5x1.5</td><td>0.75x.75 1.5x1.5</td><td>1.5x1.5</td><td>1.5x1.5</td></tr>
  <tr><td class="key">Standard Panel Size(ft.)</td><td>12x4</td><td>12.4</td><td>12.5x4</td><td>12x4</td><td>10x4, 12x4</td></tr>
  <tr><td class="key">Open Area</td><td>74%</td><td>72%</td><td>42%</td><td>69%</td><td>69%</td></tr>
  <tr><td class="key">Weight (lbs./ft.)</td><td>1.02</td><td>1.33</td><td>2.15</td><td>1.88</td><td>2.52</td></tr>
</table>
</body>
</html>
```